FLYER für Fortbildung
Zielgruppe
Die Fortbildung, die beworben werden soll, richtet sich an Fachkräfte, die in Kitas arbeiten. In diesem Fall handelt es sich um eine praxisorientierte Online-Live-Fortbildung - dies bedeutet, die TeilnehmerInnen werden während der Online-Fortbildung kontinuierlich durch eine Referentin begleitet. Die Fortbildung erweitert das Wissen und die Kompetenzen der Teilnehmenden.
Aufgabenstellung
Ich freue mich über Vorschläge eines Falzflyers im Format DIN lang. Wie viele Seiten der Flyer umfasst, überlasse ich gerne Ihnen, da dies von Ihrer Gestaltung abhängt.
Falls Sie 1-4 Bilder einfügen möchten, gebe ich Ihnen in den Datei-Upload gerne einige Beispiele, die mir zusagen (zur Auswahl). Darüber hinaus bin ich selbstverständlich auch offen für alternative Vorschläge sowie neue Designs.

```html
<!DOCTYPE html>
<html lang="de">
<head>
<meta charset="utf-8">
<title>Flyer – Elterngespräche führen</title>
<link rel="stylesheet" href="https://fonts.googleapis.com/css2?family=Montserrat:ital,wght@0,400;0,500;0,600;0,700;0,800;1,400&display=swap">
<style>
:root{
  --blue:#6f84a3;
  --blue-dark:#4f6383;
  --gold:#b08d57;
  --ink:#1d1d1f;
  --white:#ffffff;
  --paper:#e9eef5;
  --stage:#8a8a8a;
  --rule:#555555;
}
*{box-sizing:border-box;margin:0;padding:0}
html,body{width:838px;height:1200px;overflow:hidden}
body{background:var(--stage);font-family:"Montserrat",sans-serif;color:var(--ink);position:relative}
.spread{position:absolute;left:20px;width:798px;height:568px;background:var(--white);overflow:hidden}
.spread--outside{top:20px}
.spread--inside{top:612px}
.spread svg.bg{position:absolute;inset:0}
.abs{position:absolute}

/* outside */
.brand{left:440px;top:60px;width:230px;text-align:center}
.brand__name{display:flex;align-items:center;justify-content:center;gap:7px;font-size:14px;font-weight:600;color:var(--blue-dark);letter-spacing:.5px}
.brand__dot{width:12px;height:12px;border-radius:50%;background:var(--blue-dark)}
.brand__tag{font-size:6.5px;letter-spacing:2.6px;color:var(--blue);margin-top:3px}
.title{left:478px;top:378px;width:310px;text-align:center}
.title__main{font-size:27px;font-weight:800;line-height:1.02;color:var(--ink)}
.title__accent{font-size:27px;font-weight:800;line-height:1.05;color:var(--blue)}
.title__sub{font-size:17px;font-weight:500;line-height:1.2;margin-top:8px}
.title__date{display:inline-block;margin-top:9px;background:var(--blue-dark);color:var(--white);font-size:9.5px;font-weight:600;padding:4px 9px;border-radius:2px}
.contact{left:58px;top:380px;width:230px;color:var(--white)}
.contact__head{font-size:26px;font-weight:700;padding-bottom:6px;border-bottom:1.5px solid var(--white);width:215px}
.contact__phone{display:flex;align-items:center;gap:4px;font-size:27px;font-weight:600;margin-top:12px;white-space:nowrap}
.contact__line{display:flex;align-items:center;gap:6px;font-size:13px;font-weight:600;margin-top:5px;white-space:nowrap}
.contact svg{flex:none}

/* inside */
.intro{left:40px;top:226px;width:330px;font-size:10.6px;line-height:1.3;font-weight:500}
.topics{left:40px;top:318px;width:325px;height:114px;background:var(--gold);border-radius:10px;padding:8px 14px;list-style:none;color:var(--white)}
.topics li{display:flex;align-items:center;gap:7px;font-size:10.4px;font-weight:700;line-height:1.65}
.benefit{left:40px;top:480px;width:340px;color:var(--white)}
.benefit__text{font-size:10px;font-style:italic;line-height:1.3}
.benefit__fee{font-size:14.5px;font-weight:700;margin-top:3px}
.form{left:418px;top:8px;width:370px;height:552px;background:var(--white);padding:30px 30px 0}
.form__head{font-size:15px;font-weight:700;color:var(--gold);letter-spacing:.3px}
.form__event{font-size:8.5px;font-weight:700;margin-top:15px}
.form__date{font-size:7px;margin-top:4px}
.field{display:flex;align-items:flex-end;gap:5px;font-size:7px;font-weight:700;margin-top:17px}
.field--mail{margin-top:30px}
.rule{flex:1;border-bottom:.8px solid var(--rule);height:1px}
.rule-block{border-bottom:.8px solid var(--rule);margin-top:14px}
.rule-block--mail{margin-top:16px}
.form__note-head{font-size:10px;font-weight:700;color:var(--blue);margin-top:26px}
.form__note p{font-size:7px;line-height:1.3;margin-top:7px}
.signs{display:flex;justify-content:space-between;margin-top:40px}
.sign{width:140px;border-top:.8px solid var(--rule);text-align:center;font-size:7px;padding-top:4px}
</style>
</head>
<body>

<section class="spread spread--outside">
  <svg class="bg" width="798" height="568" viewBox="0 0 798 568">
    <defs>
      <linearGradient id="photoA" x1="0" y1="0" x2="1" y2="1"><stop offset="0" stop-color="#c7a77a"/><stop offset=".5" stop-color="#7f8aa6"/><stop offset="1" stop-color="#c9c3b8"/></linearGradient>
      <linearGradient id="photoB" x1="0" y1="0" x2="1" y2="1"><stop offset="0" stop-color="#e6ddd0"/><stop offset=".55" stop-color="#d9b8a6"/><stop offset="1" stop-color="#b9a89a"/></linearGradient>
      <linearGradient id="photoC" x1="0" y1="0" x2="1" y2="1"><stop offset="0" stop-color="#d8b79a"/><stop offset="1" stop-color="#8aa58c"/></linearGradient>
      <linearGradient id="photoD" x1="0" y1="0" x2="1" y2="1"><stop offset="0" stop-color="#e8e2d8"/><stop offset="1" stop-color="#b69c8c"/></linearGradient>
    </defs>
    <path d="M0 0H412C398 120 430 230 462 315H0Z" fill="url(#photoA)" role="img" aria-label="Foto: Kita-Gruppe mit Erzieherin, Kinder jubeln mit erhobenen Armen"/>
    <path d="M412 0H798V250C720 300 600 330 500 320C470 250 425 140 412 0Z" fill="url(#photoB)" role="img" aria-label="Foto: Erzieherin spielt mit Kindern am Tisch"/>
    <path d="M0 300H460C445 420 430 500 440 568H0Z" fill="var(--blue)"/>
    <path d="M408 0C392 140 470 240 455 370C445 450 425 510 436 568" fill="none" stroke="var(--gold)" stroke-width="16"/>
    <path d="M424 0C410 140 488 240 472 370C462 450 442 510 452 568" fill="none" stroke="var(--white)" stroke-width="6"/>
    <circle cx="368" cy="436" r="72" fill="var(--white)"/>
    <circle cx="368" cy="436" r="66" fill="var(--blue-dark)"/>
    <circle cx="368" cy="436" r="61" fill="url(#photoC)" role="img" aria-label="Foto: Erzieherin liest Kindern vor"/>
    <circle cx="703" cy="286" r="74" fill="var(--white)"/>
    <circle cx="703" cy="286" r="68" fill="var(--blue-dark)"/>
    <circle cx="703" cy="286" r="63" fill="url(#photoD)" role="img" aria-label="Foto: Kindergruppe im Sitzkreis"/>
  </svg>

  <div class="abs brand">
    <div class="brand__name"><span class="brand__dot"></span>KLARBLICK</div>
    <div class="brand__tag">COACHING &amp; SUPERVISION</div>
  </div>

  <div class="abs title">
    <div class="title__main">ELTERNGESPRÄCHE<br>FÜHREN –</div>
    <div class="title__accent">GRUNDLAGEN</div>
    <div class="title__sub">Live-Online-Fortbildung für<br>Mitarbeitende in Kitas</div>
    <div class="title__date">Montag, den 30. März 2026 09:00 bis 15:00 Uhr</div>
  </div>

  <div class="abs contact">
    <div class="contact__head">Kontakt</div>
    <div class="contact__phone">
      <svg width="18" height="22" viewBox="0 0 18 22"><path d="M5 2C2 3 1 6 2 10C4 15 8 19 12 20C15 21 17 19 17 17L13 14L11 16C8 15 6 12 5 9L7 7L5 2Z" fill="var(--white)"/></svg>030-555-0148
    </div>
    <div class="contact__line"><svg width="10" height="10"><circle cx="5" cy="5" r="5" fill="var(--white)"/><circle cx="5" cy="5" r="2" fill="var(--blue)"/></svg>www.klarblick-coaching.com</div>
    <div class="contact__line"><svg width="10" height="10"><circle cx="5" cy="5" r="5" fill="var(--white)"/><rect x="2.5" y="3" width="5" height="4" fill="var(--blue)"/></svg>support@klarblick-mail.de</div>
    <div class="contact__line"><svg width="10" height="12" viewBox="0 0 10 12"><path d="M5 0C2 0 0 2 0 5C0 8 5 12 5 12S10 8 10 5C10 2 8 0 5 0Z" fill="var(--white)"/><circle cx="5" cy="5" r="2" fill="var(--blue)"/></svg>12 Lindenweg, Musterstadt</div>
  </div>
</section>

<section class="spread spread--inside">
  <svg class="bg" width="798" height="568" viewBox="0 0 798 568">
    <defs>
      <linearGradient id="photoE" x1="0" y1="0" x2="1" y2="1"><stop offset="0" stop-color="#d7c6b2"/><stop offset=".5" stop-color="#b7898a"/><stop offset="1" stop-color="#9eb0c6"/></linearGradient>
    </defs>
    <rect x="400" y="0" width="398" height="568" fill="var(--paper)"/>
    <path d="M0 0H400V178C300 230 160 192 0 222Z" fill="url(#photoE)" role="img" aria-label="Foto: Erzieherin spielt mit Kindern und Tierfiguren am Tisch"/>
    <path d="M0 470C120 430 260 400 400 410V568H0Z" fill="var(--blue)"/>
    <path d="M400 445H798V568H400Z" fill="var(--blue)"/>
  </svg>

  <p class="abs intro">Diese Fortbildung richtet sich an Berufsanfänger, unsichere Fachkräfte und alle, die ihre Kenntnisse bezüglich Elterngesprächen auffrischen möchten. Ziel ist es, Ihnen Sicherheit und Selbstvertrauen im Umgang mit Eltern zu geben. Benötigt wird ein PC oder Laptop mit Webcam/Mikrofon.</p>

  <ul class="abs topics">
    <li><svg width="9" height="9"><circle cx="4.5" cy="4.5" r="4.5" fill="var(--white)"/><path d="M2.3 4.6L4 6.2L6.8 3" stroke="var(--gold)" stroke-width="1.3" fill="none"/></svg>Theoretische Modelle der Gesprächsführung</li>
    <li><svg width="9" height="9"><circle cx="4.5" cy="4.5" r="4.5" fill="var(--white)"/><path d="M2.3 4.6L4 6.2L6.8 3" stroke="var(--gold)" stroke-width="1.3" fill="none"/></svg>Effektive Vorbereitung auf Elterngespräche</li>
    <li><svg width="9" height="9"><circle cx="4.5" cy="4.5" r="4.5" fill="var(--white)"/><path d="M2.3 4.6L4 6.2L6.8 3" stroke="var(--gold)" stroke-width="1.3" fill="none"/></svg>Gesprächseinstieg</li>
    <li><svg width="9" height="9"><circle cx="4.5" cy="4.5" r="4.5" fill="var(--white)"/><path d="M2.3 4.6L4 6.2L6.8 3" stroke="var(--gold)" stroke-width="1.3" fill="none"/></svg>Umgang mit schwierigen Gesprächssituationen</li>
    <li><svg width="9" height="9"><circle cx="4.5" cy="4.5" r="4.5" fill="var(--white)"/><path d="M2.3 4.6L4 6.2L6.8 3" stroke="var(--gold)" stroke-width="1.3" fill="none"/></svg>Deeskalation / Konfliktlösungsstrategien</li>
    <li><svg width="9" height="9"><circle cx="4.5" cy="4.5" r="4.5" fill="var(--white)"/><path d="M2.3 4.6L4 6.2L6.8 3" stroke="var(--gold)" stroke-width="1.3" fill="none"/></svg>Möglichkeiten zum Üben und Austausch</li>
  </ul>

  <div class="abs benefit">
    <p class="benefit__text">Profitieren Sie von praxisnahen Tipps und Übungen, die Ihnen helfen, Ihre Kommunikationsfähigkeiten zu stärken und schwierige Situationen souverän zu meistern.</p>
    <p class="benefit__fee">Teilnahmegebühr: 99, 00 € pro Person</p>
  </div>

  <div class="abs form">
    <h2 class="form__head">ANMELDUNG ZUR FORTBILDUNG</h2>
    <p class="form__event">Elterngespräche führen – Grundlagen</p>
    <p class="form__date">am 30. März 2025 von 09:00 – 15:00 Uhr (online)</p>
    <div class="field">Vor- und Zuname:<span class="rule"></span></div>
    <div class="field">Rechnungsadresse:<span class="rule"></span></div>
    <div class="rule-block"></div>
    <div class="rule-block"></div>
    <div class="rule-block"></div>
    <div class="field field--mail">Ihre E-Mail-Adresse für den Zugangslink:</div>
    <div class="rule-block rule-block--mail"></div>
    <div class="form__note">
      <h3 class="form__note-head">Hinweise:</h3>
      <p>Bitte füllen Sie das Formular aus und senden Sie es an info@klarblick-coaching.de.</p>
      <p>Sobald uns Ihre Anmeldung vorliegt, erhalten Sie die Zahlungsinformationen. Die Teilnahmegebühr beträgt 99,00 € pro Person. Bitte beachten Sie, dass Plätze, für die keine Zahlungen geleistet werden, an andere Interessierte weitergegeben werden.</p>
      <p>Der Zugangslink wird Ihnen eine Woche vor Beginn der Veranstaltung zugesandt.</p>
      <p>Mit Ihrer Anmeldung erklären Sie sich mit unseren AGB einverstanden. Sie stimmen außerdem zu, dass wir Ihre personenbezogenen Daten, darunter Name, E-Mail-Adresse sowie Datum und Titel der besuchten Veranstaltung verwenden. Zudem stimmen Sie zu, dass wir Sie über interessante Fortbildungsangebote informieren dürfen. Diese Zustimmung können Sie jederzeit widerrufen.</p>
    </div>
    <div class="signs">
      <div class="sign">Ort, Datum</div>
      <div class="sign">Unterschrift</div>
    </div>
  </div>
</section>

</body>
</html>
```